Stationary Set Rebrand for Brenvik

We are a Canadian Distribution and Service Company that was established in 1969. Over the past 5 decades we have expanded our business and have warehouses across Canada. We specialize in adhesive tapes, adhesives, films, safety, warehouse, shipping, janitorial and packaging supplies.

We have updated our logo design and would like a new corporate branding identity that includes a new fresh Stationary Set (Business Cards, Letterhead, Letterhead MS Word, Envelope, Presentation Folders, Email Signatures, Notepad Covers, etc.)

Target Market(s)

Industrial Business Sector

Font styles to use
Sans Serif

Colors
0054AA
0677BA
7BADD7
CADEEF
E8F1F8
0094D4
00A9DD
6FCCEA
C7EBF8
E9F6FB
00AB8E
00BBA5
67D7C9
C6EFE9
E9F9F6
EB3D1F
EC4F4E
F09395
F8D3D4
FCEDEE

Requirements
Should not have
• Colors not too light, darker colours preferred

```html
<!DOCTYPE html>
<html lang="en">
<head>
<meta charset="utf-8">
<title>Brenvik Business Card</title>
<link href="https://fonts.googleapis.com/css2?family=Saira:wght@400;500;800&family=Michroma&display=swap" rel="stylesheet">
<style>
  :root {
    --stage: #d9d9d9;
    --card-dark: #313131;
    --card-light: #ffffff;
    --brand-red: #d71920;
    --ink: #1c1a1b;
    --white: #ffffff;
  }
  html, body {
    margin: 0;
    padding: 0;
    width: 1200px;
    height: 1200px;
    overflow: hidden;
    background: var(--stage);
    font-family: "Saira", Arial, sans-serif;
  }
  .stage {
    position: relative;
    width: 1200px;
    height: 1200px;
  }
  .card {
    position: absolute;
    left: 252px;
    width: 696px;
    height: 397px;
    box-sizing: border-box;
  }
  .card--front { top: 156px; background: var(--card-dark); color: var(--white); }
  .card--back  { top: 651px; background: var(--card-light); color: var(--ink); }

  .wordmark {
    position: absolute;
    display: flex;
    align-items: center;
    gap: 10px;
  }
  .wordmark__name {
    font-weight: 800;
    line-height: 1;
    letter-spacing: -1px;
  }
  .wordmark__dot {
    border-radius: 50%;
    background: var(--brand-red);
    flex: none;
  }
  .tagline {
    position: absolute;
    font-weight: 500;
    line-height: 1;
  }

  .card--front .wordmark { left: 42px; top: 48px; }
  .card--front .wordmark__name { font-size: 62px; color: var(--white); }
  .card--front .wordmark__dot { width: 14px; height: 14px; }
  .card--front .tagline { left: 42px; top: 110px; font-size: 14px; color: var(--white); }

  .holder { position: absolute; left: 42px; top: 158px; }
  .holder__name {
    font-family: "Michroma", Arial, sans-serif;
    font-size: 20px;
    color: var(--brand-red);
    letter-spacing: 0.5px;
    margin: 0;
    line-height: 1.2;
  }
  .holder__role { font-size: 15px; margin: 2px 0 0; letter-spacing: 0.5px; }

  .address {
    position: absolute;
    left: 42px;
    top: 222px;
    font-size: 16px;
    line-height: 21px;
    letter-spacing: 0.6px;
    font-style: normal;
  }
  .contacts {
    position: absolute;
    left: 42px;
    top: 276px;
    margin: 0;
    padding: 0;
    list-style: none;
    font-size: 16px;
    letter-spacing: 0.6px;
  }
  .contacts li {
    display: flex;
    align-items: center;
    height: 21px;
  }
  .contacts svg { width: 14px; height: 14px; margin-right: 14px; fill: var(--brand-red); }

  .feature-art {
    position: absolute;
    left: 334px;
    top: 31px;
    width: 340px;
    height: 340px;
    border-radius: 50%;
    background: var(--brand-red);
  }

  .card--back .wordmark { left: 146px; top: 140px; }
  .card--back .wordmark__name { font-size: 96px; color: var(--ink); }
  .card--back .wordmark__dot { width: 22px; height: 22px; }
  .card--back .tagline { left: 148px; top: 236px; font-size: 21px; color: var(--ink); }
</style>
</head>
<body>
<main class="stage">
  <section class="card card--front">
    <div class="wordmark">
      <span class="wordmark__name">Brenvik</span>
      <span class="wordmark__dot"></span>
    </div>
    <div class="tagline">Tape and Packaging Specialists</div>

    <div class="holder">
      <h1 class="holder__name">MARTA ELLISON</h1>
      <p class="holder__role">President</p>
    </div>

    <address class="address">4120 Cedarfield Road<br>Kelmont, Canada 20418</address>

    <ul class="contacts">
      <li>
        <svg viewBox="0 0 24 24" aria-hidden="true"><path d="M6.6 10.8a15.1 15.1 0 0 0 6.6 6.6l2.2-2.2c.3-.3.7-.4 1-.2 1.1.4 2.3.6 3.6.6.6 0 1 .4 1 1V20c0 .6-.4 1-1 1A17 17 0 0 1 3 4c0-.6.4-1 1-1h3.5c.6 0 1 .4 1 1 0 1.3.2 2.5.6 3.6.1.3 0 .7-.2 1z"/></svg>
        555-204-1187
      </li>
      <li>
        <svg viewBox="0 0 24 24" aria-hidden="true"><path d="M7 1h10a2 2 0 0 1 2 2v18a2 2 0 0 1-2 2H7a2 2 0 0 1-2-2V3a2 2 0 0 1 2-2zm0 3v14h10V4zm5 15.5a1 1 0 1 0 0 2 1 1 0 0 0 0-2z"/></svg>
        555-318-9042
      </li>
      <li>
        <svg viewBox="0 0 24 24" aria-hidden="true"><path d="M2 5h20v14H2zm2 2v.5l8 5 8-5V7zm0 2.8V17h16V9.8l-8 5z"/></svg>
        info@brenvik.com
      </li>
      <li>
        <svg viewBox="0 0 24 24" aria-hidden="true"><path d="M12 2a10 10 0 1 0 0 20 10 10 0 0 0 0-20zm-1 17.9A8 8 0 0 1 4.1 11H7c.1 3 1.4 6 4 8.9zM4.1 9A8 8 0 0 1 11 4.1C8.9 6.3 7.6 7.8 7.3 9zm9-4.9A8 8 0 0 1 19.9 11H17c-.2-2.8-1.5-5-3.9-6.9zM13 19.9c2-2.3 3.5-4.8 3.9-6.9h3A8 8 0 0 1 13 19.9z"/></svg>
        www.brenvik.com
      </li>
    </ul>

    <div class="feature-art" role="img" aria-label="Large red brand emblem decoration"></div>
  </section>

  <section class="card card--back">
    <div class="wordmark">
      <span class="wordmark__name">Brenvik</span>
      <span class="wordmark__dot"></span>
    </div>
    <div class="tagline">Tape and Packaging Specialists</div>
  </section>
</main>
</body>
</html>
```